Redesign of existing business card

I would like the "signage" attachment converted into a business card. This needs to be double sided aswell, keeping the phone number and names on the front, and the email + website on the back.

Second attachment is the current business card design.

Larger font for contact details is required.

Must keep to original color themes (electric blue, silver/grey etc)

Back of the card to have blue background with white writing.

Industry/Entity Type

Business

Contact Information for Business Card

Refer to existing design from attachments

Requirements
Must have
• Refer to existing design from attachments
Nice to have

```html
<!DOCTYPE html>
<html lang="en">
<head>
<meta charset="utf-8">
<title>Volta Spark Services – Business Card</title>
<link rel="stylesheet" href="https://fonts.googleapis.com/css2?family=Roboto+Condensed:wght@400;700&display=swap">
<style>
  :root {
    --electric-blue: #1f1ff2;
    --deep-blue: #1212b8;
    --silver: #c3c7cf;
    --silver-dark: #8e939c;
    --white: #ffffff;
    --page: #e9eaee;
    --shadow: rgba(20, 20, 60, 0.18);
  }
  * { box-sizing: border-box; margin: 0; padding: 0; }
  html, body {
    width: 1200px; height: 950px; overflow: hidden;
    background: var(--page);
    font-family: "Roboto Condensed", "Arial Narrow", sans-serif;
  }
  .sheet {
    width: 1200px; height: 950px;
    display: flex; flex-direction: column; align-items: center; justify-content: center;
    gap: 30px;
  }
  .card {
    position: relative;
    width: 760px; height: 434px;
    border-radius: 24px;
    overflow: hidden;
    box-shadow: 0 10px 26px var(--shadow);
  }
  /* Front */
  .card-front { background: var(--white); }
  .front-swoosh { position: absolute; inset: 0; width: 100%; height: 100%; }
  .brand {
    position: absolute; left: 90px; top: 110px;
    display: flex; align-items: center; gap: 18px;
  }
  .brand-dot {
    width: 64px; height: 64px; border-radius: 50%;
    background: var(--electric-blue);
  }
  .brand-name {
    color: var(--electric-blue);
    font-weight: 700; font-size: 46px; line-height: 1; letter-spacing: 1px;
    text-transform: uppercase;
  }
  .contact {
    position: absolute; right: 56px; bottom: 54px;
    color: var(--white); text-align: left;
  }
  .contact-name { font-size: 30px; font-weight: 400; letter-spacing: 0.5px; }
  .contact-phone {
    margin-top: 10px; font-size: 30px; letter-spacing: 1px;
    display: flex; align-items: center; gap: 10px;
  }
  .phone-icon { width: 28px; height: 28px; }
  /* Back */
  .card-back {
    background: linear-gradient(160deg, var(--electric-blue) 0%, var(--deep-blue) 100%);
    color: var(--white);
  }
  .back-mark {
    position: absolute; left: 50%; top: 46%;
    transform: translate(-50%, -50%);
    display: flex; align-items: center; gap: 18px;
  }
  .back-dot {
    width: 70px; height: 70px; border-radius: 50%;
    background: var(--silver);
  }
  .back-name {
    font-weight: 700; font-size: 44px; letter-spacing: 1px; text-transform: uppercase;
  }
  .back-details {
    position: absolute; left: 0; right: 0; bottom: 36px;
    text-align: center; font-size: 24px; letter-spacing: 0.5px;
  }
</style>
</head>
<body>
<main class="sheet">
  <section class="card card-front" aria-label="Business card front">
    <svg class="front-swoosh" viewBox="0 0 760 434" preserveAspectRatio="none" aria-hidden="true">
      <path d="M0 300 C 260 300, 560 250, 760 110 L760 434 L0 434 Z" fill="var(--silver)"/>
      <path d="M0 318 C 260 318, 570 272, 760 132 L760 434 L0 434 Z" fill="var(--silver-dark)"/>
      <path d="M0 326 C 260 326, 575 284, 760 146 L760 434 L0 434 Z" fill="var(--electric-blue)"/>
    </svg>
    <div class="brand">
      <span class="brand-dot"></span>
      <span class="brand-name">Volta Spark Services</span>
    </div>
    <div class="contact">
      <p class="contact-name">Liam Carter – CEO&amp;Founder</p>
      <p class="contact-phone">
        <svg class="phone-icon" viewBox="0 0 24 24" aria-hidden="true">
          <circle cx="12" cy="12" r="11" fill="var(--white)"/>
          <path d="M8.2 6.5c.4-.3 1-.2 1.3.2l1.2 1.8c.3.4.2.9-.1 1.2l-.8.7c.5 1.2 1.5 2.4 2.8 3.1l.7-.8c.3-.4.9-.4 1.2-.1l1.8 1.2c.4.3.5.9.2 1.3l-.7.9c-.5.6-1.3.8-2 .5-2.9-1.2-5.1-3.5-6.2-6.3-.3-.7 0-1.5.5-2z" fill="var(--electric-blue)"/>
        </svg>
        0400 555 123
      </p>
    </div>
  </section>

  <section class="card card-back" aria-label="Business card back">
    <div class="back-mark">
      <span class="back-dot"></span>
      <span class="back-name">Volta Spark Services</span>
    </div>
    <p class="back-details">info@voltaspark.com.au | www.voltaspark.com.au</p>
  </section>
</main>
</body>
</html>
```